Verdant Medispa Business Card

need a business card for our medispa, attached please see the logo.
our website is https://verdantmedispa-example.com

Sorina Belcourt, MD
Internal Medicine

555-204-7193

Sorina@verdantmedispa-example.com

Www.Verdantmedispa-example.com

738 E Harlow Blvd N, Ste 512, Katy, TX 77981

Target Market(s)

MedSpa, Cosmetics, Esthetics

Industry/Entity Type

MedicalSpa

Contact Information for Business Card

Please see the attached business card which i pulled from the internet. I like the idea back as a logo and front with info.

Font styles to use
Decorative

Requirements
Must have
• Color should be matching with Logo and Website theme, Also I like to have QR code for the website

```html
<!DOCTYPE html>
<html lang="en">
<head>
<meta charset="utf-8">
<title>Verdant Medispa Business Card</title>
<link href="https://fonts.googleapis.com/css2?family=Cinzel+Decorative:wght@700&family=Roboto:wght@400&display=swap" rel="stylesheet">
<style>
  :root {
    --gold: #c9a227;
    --gold-light: #f0d65a;
    --gold-dark: #b48d1c;
    --ink: #1e1e1e;
    --card-dark: #181818;
    --paper: #ffffff;
  }
  * { margin: 0; padding: 0; box-sizing: border-box; }
  html, body { width: 1200px; height: 896px; overflow: hidden; background: var(--paper); }
  .stage { position: relative; width: 1200px; height: 896px; }
  .card {
    position: absolute; left: 334px; width: 527px; height: 302px;
    border-radius: 30px; overflow: hidden;
  }
  .card--front { top: 125px; background: var(--paper); border: 1px solid #e6e6e6; }
  .card--back { top: 471px; background: var(--card-dark); }

  .brand {
    position: absolute; left: 0; right: 0; text-align: center;
    font-family: "Cinzel Decorative", serif; font-weight: 700; color: var(--gold);
  }
  .card--front .brand { top: 58px; font-size: 38px; }
  .card--back .brand { top: 118px; font-size: 48px; }
  .brand-dot {
    display: inline-block; width: 10px; height: 10px; border-radius: 50%;
    background: var(--gold); vertical-align: middle; margin-right: 10px;
  }

  .holder { position: absolute; right: 276px; top: 178px; text-align: right; }
  .holder-name {
    font-family: "Cinzel Decorative", serif; font-weight: 700; font-size: 19px;
    color: var(--gold); white-space: nowrap;
  }
  .holder-title {
    margin-top: 20px; font-family: Roboto, sans-serif; font-size: 12.5px; color: var(--ink);
  }
  .divider { position: absolute; left: 263px; top: 180px; width: 1px; height: 54px; background: var(--gold); }

  .contact { position: absolute; left: 272px; top: 178px; list-style: none; }
  .contact li {
    display: flex; align-items: center; gap: 4px; height: 20px;
    font-family: Roboto, sans-serif; font-size: 12.5px; color: var(--ink); white-space: nowrap;
  }
  .contact svg { width: 11px; height: 11px; flex: none; }

  .address-band {
    position: absolute; left: 0; right: 0; top: 265px; height: 18px;
    background: linear-gradient(180deg, var(--gold-dark), var(--gold-light) 45%, var(--gold-dark));
    font-family: Roboto, sans-serif; font-size: 12px; line-height: 18px;
    text-align: center; color: var(--ink);
  }
</style>
</head>
<body>
<main class="stage">
  <section class="card card--front">
    <div class="brand"><span class="brand-dot"></span>Verdant Medispa</div>

    <div class="holder">
      <div class="holder-name">Sorina Belcourt, MD</div>
      <div class="holder-title">Internal Medicine</div>
    </div>
    <div class="divider"></div>

    <ul class="contact">
      <li>
        <svg viewBox="0 0 12 12" aria-hidden="true"><path d="M2.5 1 L4.5 1 L5.2 3.6 L3.9 4.6 Q5 7 7.4 8.1 L8.4 6.8 L11 7.5 L11 9.5 Q10.5 11 9 11 Q1 10 1 3 Q1 1.5 2.5 1 Z" fill="var(--gold)"/></svg>
        555-204-7193
      </li>
      <li>
        <svg viewBox="0 0 12 12" aria-hidden="true"><rect x="0.5" y="2.5" width="11" height="7.5" fill="var(--gold)"/><path d="M0.5 2.5 L6 7 L11.5 2.5" fill="none" stroke="#fff" stroke-width="0.9"/></svg>
        Sorina@verdantmedispa-example.com
      </li>
      <li>
        <svg viewBox="0 0 12 12" aria-hidden="true"><circle cx="6" cy="6" r="5.2" fill="var(--gold)"/><path d="M1 6 H11 M6 0.8 Q3 6 6 11.2 M6 0.8 Q9 6 6 11.2" fill="none" stroke="#fff" stroke-width="0.8"/></svg>
        Www.Verdantmedispa-example.com
      </li>
    </ul>

    <div class="address-band">738 E Harlow Blvd N, Ste 512, Katy, TX 77981</div>
  </section>

  <section class="card card--back">
    <div class="brand"><span class="brand-dot"></span>Verdant Medispa</div>
  </section>
</main>
</body>
</html>
```